Van Wrap Designer to Make Heads Turn!

Brellwick Electrical is revving up for a bold new look – and we want YOU to take the wheel.

We're searching for a visionary designer to completely reimagine our company van wraps. This isn’t just a facelift – it’s a full-on brand evolution. We want designs that turn heads, spark conversations, and stop people in their tracks. This might be a bold statement about quality - we are ok with being cheeky.

What We're Looking For:
Bold, modern, unforgettable wrap designs that command attention on the road.

Primary focus on the Brellwick Electrical brand — this is our flagship, and it needs to shine.

Subtle but impactful inclusion of our sister brands:
Brellwick Group
Brellwick Property Solutions
Brellwick Energy Solutions
These should be incorporated, likely toward the back of the van, while keeping the overall design cohesive.

Your Mission:
Elevate our visual presence, we have had the same wraps for 11 years, it's time for something new and exciting.
Design is for a 2025 Marvento Kestel

Inject a fresh, forward-thinking look that feels professional but far from boring.

Deliver a print-ready design by September 1, 2025.

Work collaboratively with our team to ensure brand consistency across all elements.

You Might Be the One If:
You have a strong portfolio of vehicle wrap or large-format design work.
You know how to blend brand identity with real-world impact.
You love pushing creative limits while still delivering clean, purposeful design.

Our current wrap is attached for reference — but we’re ready to up the ante. Think bigger, bolder, and more engaging.

Ready to leave your mark all over town (literally)?
Apply now with your portfolio and tell us how you’ll make our vans the talk of the street.

Requirements
Must have
• Logos, Phone number, company branding and colours

```html
<!DOCTYPE html>
<html lang="en">
<head>
<meta charset="utf-8">
<title>Brellwick Electrical – Van Wrap Concepts</title>
<link href="https://fonts.googleapis.com/css2?family=Archivo+Black&family=Oswald:wght@500&family=Poppins:wght@600;700&display=swap" rel="stylesheet">
<style>
  :root{
    --canvas:#ecedee;
    --wrap-white:#f1f0eb;
    --ink:#121212;
    --gold:#c99a2e;
    --gold-light:#e6c25c;
    --gold-dark:#9c7218;
    --glass:#3a3d42;
    --trim:#2a2b2e;
    --tyre:#1b1b1d;
    --rim:#c9cbcf;
    --light-red:#b3262d;
  }
  html,body{margin:0;padding:0;overflow:hidden}
  body{width:1200px;height:1200px;background:var(--canvas);position:relative}
  .van-wrap{position:absolute;left:75px;width:1050px;height:425px}
  .van-wrap--side-a{top:125px}
  .van-wrap--side-b{top:637px}
  .brand-name{font-family:"Archivo Black",sans-serif;fill:var(--ink);font-size:31px}
  .tagline{font-family:"Poppins",sans-serif;font-weight:700;font-size:10.5px;fill:var(--ink)}
  .web{font-family:"Poppins",sans-serif;font-weight:600;font-size:12px;fill:var(--ink)}
  .web--light{fill:#ffffff;font-size:14px;letter-spacing:.5px}
  .call-label{font-family:"Poppins",sans-serif;font-weight:700;font-size:11px;fill:var(--gold)}
  .phone{font-family:"Poppins",sans-serif;font-weight:700;font-size:19px;fill:var(--ink)}
  .phone--small{font-size:15px}
  .audience{font-family:"Oswald",sans-serif;font-weight:500;font-size:13px;fill:var(--gold-light);letter-spacing:.4px}
  .audience--list{font-size:12px;fill:var(--gold)}
</style>
</head>
<body>

<svg class="van-wrap van-wrap--side-a" viewBox="60 100 840 340" role="group" aria-label="Brellwick Electrical van wrap, layout one">
  <defs>
    <linearGradient id="goldA" x1="0" y1="0" x2="1" y2="1">
      <stop offset="0" stop-color="var(--gold-light)"/>
      <stop offset=".5" stop-color="var(--gold)"/>
      <stop offset="1" stop-color="var(--gold-dark)"/>
    </linearGradient>
  </defs>
  <path class="body" fill="var(--wrap-white)" d="M72 270 Q80 240 130 225 L230 160 Q260 130 330 123 L840 122 Q868 124 872 160 L878 350 L878 385 L772 385 A58 58 0 0 0 656 385 L268 385 A58 58 0 0 0 152 385 L70 385 Z"/>
  <polygon class="roof-swoosh" fill="var(--ink)" points="72,270 130,225 230,160 330,123 840,122 860,128 440,215 300,250 140,272"/>
  <polygon class="gold-accent" fill="url(#goldA)" points="140,285 360,250 165,292"/>
  <path class="gold-band" fill="url(#goldA)" d="M262 345 L878 278 L878 385 L772 385 A58 58 0 0 0 656 385 L268 385 Z"/>
  <polygon class="black-stripe" fill="var(--ink)" points="262,352 878,290 878,320 266,382"/>
  <path class="window" fill="var(--glass)" d="M205 205 L262 152 L420 140 L420 232 L205 240 Z"/>
  <rect class="front-bumper" fill="var(--trim)" x="70" y="330" width="70" height="55" rx="6"/>
  <rect class="rear-bumper" fill="var(--trim)" x="860" y="345" width="20" height="40"/>
  <rect class="tail-light" fill="var(--light-red)" x="866" y="210" width="12" height="60" rx="2"/>
  <g class="wheel"><circle cx="210" cy="382" r="48" fill="var(--tyre)"/><circle cx="210" cy="382" r="32" fill="var(--rim)"/></g>
  <g class="wheel"><circle cx="714" cy="382" r="48" fill="var(--tyre)"/><circle cx="714" cy="382" r="32" fill="var(--rim)"/></g>

  <text class="web" x="600" y="195">www.brellwickelectrical.com.au</text>
  <rect class="brand-square" fill="var(--gold)" x="468" y="204" width="62" height="62"/>
  <text class="brand-name" x="545" y="229">BRELLWICK</text>
  <text class="brand-name" x="545" y="261">ELECTRICAL</text>
  <text class="tagline" x="588" y="277">WE'LL BE THERE IN YOUR DARKEST HOUR!</text>
  <text class="call-label" x="255" y="294">CALL :</text>
  <text class="phone" x="256" y="318">(08) 5550 3017</text>
  <text class="audience" x="478" y="349" transform="rotate(-5.8 478 349)">HOMEOWNERS • BUILDERS • REAL ESTATE • CONVEYANCERS</text>
</svg>

<svg class="van-wrap van-wrap--side-b" viewBox="60 100 840 340" role="group" aria-label="Brellwick Electrical van wrap, layout two">
  <defs>
    <linearGradient id="goldB" x1="0" y1="0" x2="1" y2="1">
      <stop offset="0" stop-color="var(--gold-light)"/>
      <stop offset=".5" stop-color="var(--gold)"/>
      <stop offset="1" stop-color="var(--gold-dark)"/>
    </linearGradient>
  </defs>
  <path class="body" fill="var(--wrap-white)" d="M72 270 Q80 240 130 225 L230 160 Q260 130 330 123 L840 122 Q868 124 872 160 L878 350 L878 385 L772 385 A58 58 0 0 0 656 385 L268 385 A58 58 0 0 0 152 385 L70 385 Z"/>
  <polygon class="roof-swoosh" fill="var(--ink)" points="72,270 130,225 230,160 330,123 840,122 860,128 440,215 300,250 140,272"/>
  <polygon class="gold-accent" fill="url(#goldB)" points="140,285 360,250 165,292"/>
  <path class="gold-band" fill="url(#goldB)" d="M262 345 L878 278 L878 385 L772 385 A58 58 0 0 0 656 385 L268 385 Z"/>
  <polygon class="black-stripe" fill="var(--ink)" points="262,352 878,290 878,320 266,382"/>
  <path class="window" fill="var(--glass)" d="M205 205 L262 152 L420 140 L420 232 L205 240 Z"/>
  <rect class="front-bumper" fill="var(--trim)" x="70" y="330" width="70" height="55" rx="6"/>
  <rect class="rear-bumper" fill="var(--trim)" x="860" y="345" width="20" height="40"/>
  <rect class="tail-light" fill="var(--light-red)" x="866" y="210" width="12" height="60" rx="2"/>
  <g class="wheel"><circle cx="210" cy="382" r="48" fill="var(--tyre)"/><circle cx="210" cy="382" r="32" fill="var(--rim)"/></g>
  <g class="wheel"><circle cx="714" cy="382" r="48" fill="var(--tyre)"/><circle cx="714" cy="382" r="32" fill="var(--rim)"/></g>

  <text class="contact-line" x="620" y="196"><tspan class="call-label">CALL : </tspan><tspan class="phone phone--small">(08) 5550 3017</tspan></text>
  <rect class="brand-square" fill="var(--gold)" x="468" y="204" width="62" height="62"/>
  <text class="brand-name" x="545" y="229">BRELLWICK</text>
  <text class="brand-name" x="545" y="261">ELECTRICAL</text>
  <text class="tagline" x="588" y="277">WE'LL BE THERE IN YOUR DARKEST HOUR!</text>
  <g class="audience-list">
    <circle cx="278" cy="276" r="2.4" fill="var(--ink)"/><text class="audience audience--list" x="285" y="280">HOMEOWNERS</text>
    <circle cx="278" cy="292" r="2.4" fill="var(--ink)"/><text class="audience audience--list" x="285" y="296">BUILDERS</text>
    <circle cx="278" cy="308" r="2.4" fill="var(--ink)"/><text class="audience audience--list" x="285" y="312">REAL ESTATE</text>
    <circle cx="278" cy="324" r="2.4" fill="var(--ink)"/><text class="audience audience--list" x="285" y="328">CONVEYANCERS</text>
  </g>
  <text class="web web--light" x="520" y="346" transform="rotate(-5.8 520 346)">www.brellwickelectrical.com.au</text>
</svg>

</body>
</html>
```